New Interfaces

The software open with 3 open tabs, you can see the interfaces following this steps:

Zonvia:
Select tab "Zonvia" and click on "Zonvia" in menu on the top.

KPI :
Select tab "KPI" and click on go button.

Report:
Select tab "Report" and Click on go button.

Current software: http://plexora.kelvoxsoft.net/plexora_developers/default.aspx

user: review_guest
pass: lumbrak

......

About the company

The Kelvox is a technology company that provides planning, optimization services and software to develop the market for telecom operators.

The Product

Plexora is a web management and optimization tool for mobile networks.

The project

To always offer the best experience of usability and comfort for our customers, we are remodeling our software. The goal is to have agile, modern and with special attention to usability interfaces.

user: review_guest
pass: lumbrak
Updates

Hi! We are analyzing all interfaces, we send news soon. Thank you!

Target Market(s)

Telecommunications Engineers.

Industry/Entity Type

Software

Font styles to use
Sans Serif

Requirements
Nice to have
• Attention for usability and good concept.
Should not have
• Many colors.

```html
<!DOCTYPE html>
<html lang="en">
<head>
<meta charset="utf-8">
<title>Plexora – Account Preferences &amp; Trouble Tickets</title>
<link href="https://fonts.googleapis.com/css2?family=Open+Sans:wght@400;600;700&display=swap" rel="stylesheet">
<style>
:root{
  --bar-top:#efefef;
  --bar-bottom:#dcdcdc;
  --navy:#2e3b52;
  --side-tab:#4b5b75;
  --orange:#f5b247;
  --blue:#1565c0;
  --link:#1a3f9c;
  --teal:#b9dcdc;
  --panel:#f2f2f2;
  --text:#555;
  --dark:#333;
  --red-row:#ff6b6b;
  --lav-row:#e5e5f8;
  --line:#cfcfcf;
  --footer:#4a4a4a;
}
*{box-sizing:border-box;margin:0;padding:0}
html,body{width:1200px;height:1092px;overflow:hidden}
body{position:relative;font-family:"Open Sans",sans-serif;color:var(--text);background:#fff;font-size:10px}
.abs{position:absolute}
.topbar{left:0;top:0;width:1200px;height:49px;background:linear-gradient(var(--bar-top),var(--bar-bottom));border-bottom:1px solid #ccc}
.search{left:45px;top:11px;width:151px;height:26px;background:#fff;border:1px solid #ddd;font-size:9.5px;color:#aaa;padding:6px 10px}
.search-btn{left:168px;top:11px;width:28px;height:26px;background:#7a7a7a}
.nav{top:19px;font-size:9.5px;color:#555;display:flex;align-items:center;gap:4px}
.nav svg{width:9px;height:9px}
.logoff{color:var(--link);font-weight:600}
.sidebar{left:0;top:49px;width:36px;height:974px;background:var(--navy)}
.vtab{left:0;width:24px;color:#fff;font-size:8.5px;writing-mode:vertical-rl;display:flex;align-items:center;justify-content:center;letter-spacing:.3px}
.tree{left:36px;top:49px;width:186px;height:974px;border-right:2px solid #e3e3e3}
.treemode{left:49px;top:63px;font-size:10px;color:#777}
.treemode b{color:var(--blue);font-weight:600}
.brand{left:53px;top:104px;font-size:24px;font-weight:700;color:var(--blue)}
.node{font-size:8.5px;color:#111;display:flex;align-items:center;gap:3px;white-space:nowrap}
.node .pm{width:7px;height:7px;border:1px solid #888;font-size:7px;line-height:5px;text-align:center;color:#444}
.node .ico{width:9px;height:9px;background:#8aa;display:inline-block}
.folder{width:13px;height:9px;background:#f5c857;border:1px solid #d59b2a;display:inline-block;border-radius:1px}
.big{font-size:10.5px;color:#333}
.hl{background:#f5a623;padding:0 2px}
.tabstrip{top:61px;height:23px;font-size:9.5px;display:flex;align-items:center;justify-content:center}
.prefs-outer{left:238px;top:84px;width:935px;height:302px;background:var(--panel)}
.prefs-teal{left:247px;top:99px;width:917px;height:274px;background:var(--teal)}
.prefs-white{left:255px;top:139px;width:900px;height:223px;background:#fff}
.ptitle{left:258px;top:114px;font-size:10.5px;color:#444}
.save{left:412px;top:109px;width:52px;height:21px;background:#555;color:#fff;font-size:9.5px;text-align:center;line-height:21px}
.itab{top:152px;height:26px;font-size:9.5px;text-align:center;line-height:26px;background:#eee;color:#555}
.itab.on{background:var(--orange);color:#333}
.tabline{left:264px;top:178px;width:881px;height:1px;background:#ddd}
.lbl{font-size:9.5px;color:#555;line-height:15px}
.inp{width:161px;height:28px;border:1px solid #ccc;background:#fff}
.radio{font-size:8.5px;color:#555;display:flex;align-items:center;gap:4px}
.radio i{width:7px;height:7px;border:1px solid #999;border-radius:50%;display:inline-block;position:relative}
.radio i.on::after{content:"";position:absolute;left:1.5px;top:1.5px;width:2px;height:2px;border-radius:50%;background:#334}
.submit{left:941px;top:286px;width:96px;height:35px;background:var(--orange);color:#333;font-size:10.5px;font-weight:600;text-align:center;line-height:35px}
.tt-head{left:238px;top:402px;width:937px;height:42px;background:linear-gradient(#f1f1f1,#dedede);font-size:10.5px;color:#444;padding:13px 14px}
.btn{top:458px;height:19px;border:1px solid #ccc;background:#eee;font-size:8.5px;color:#444;line-height:17px;text-align:center}
.field{left:522px;top:458px;width:102px;height:19px;border:1px solid #ccc}
.bar{left:238px;width:937px;height:42px;background:var(--teal);font-size:11.5px;color:#333;padding:11px 16px;display:flex;align-items:center;gap:9px}
.filter{left:238px;top:596px;width:937px;text-align:center;font-size:11px;font-weight:600;color:var(--blue)}
table{position:absolute;left:238px;top:621px;width:937px;border-collapse:collapse;table-layout:fixed;font-size:10.5px}
th{height:47px;background:#dcdcdc;font-weight:400;color:#444;border-right:1px solid #eee}
td{height:46.5px;text-align:center;border-right:1px solid #ddd;line-height:16px;color:#444;border-bottom:1px solid #eee}
tr.red td{background:var(--red-row);color:#fff;border-right-color:#ffdada}
tr.lav td{background:var(--lav-row)}
.chk{display:inline-block;width:8px;height:8px;background:#ddd;border:1px solid #ccc}
tr.red .chk{background:#fff}
.footer{left:0;top:1023px;width:1200px;height:69px;background:var(--footer);color:#fff;font-size:10.5px}
</style>
</head>
<body>

<div class="abs topbar"></div>
<div class="abs search">Search..</div>
<div class="abs search-btn"><svg width="28" height="26" viewBox="0 0 28 26"><circle cx="13" cy="12" r="4" fill="none" stroke="#fff" stroke-width="1.6"/><line x1="16" y1="15" x2="19" y2="18" stroke="#fff" stroke-width="1.8"/></svg></div>

<div class="abs nav" style="left:225px"><svg viewBox="0 0 10 10"><circle cx="5" cy="5" r="3.5" fill="none" stroke="#555" stroke-width="2"/></svg>Configure</div>
<div class="abs nav" style="left:301px"><svg viewBox="0 0 10 10"><rect x="1" y="6" width="2" height="4" fill="#555"/><rect x="4" y="3" width="2" height="7" fill="#555"/><rect x="7" y="0" width="2" height="10" fill="#555"/></svg>Statistics</div>
<div class="abs nav" style="left:378px"><svg viewBox="0 0 10 10"><circle cx="5" cy="5" r="4.5" fill="#555"/></svg>Planned Network</div>
<div class="abs nav" style="left:488px"><svg viewBox="0 0 10 10"><path d="M8 3A4 4 0 1 0 9 6" fill="none" stroke="#555" stroke-width="1.5"/></svg>Main KPIs</div>
<div class="abs nav" style="left:569px"><svg viewBox="0 0 10 10"><rect x="2" y="0" width="6" height="10" fill="#555"/></svg>Report</div>
<div class="abs nav" style="left:643px"><svg viewBox="0 0 10 10"><path d="M5 10L1.5 4.5A3.5 3.5 0 1 1 8.5 4.5Z" fill="#555"/></svg>Zonvia</div>
<div class="abs nav" style="left:718px"><svg viewBox="0 0 10 10"><rect x="0" y="2" width="10" height="7" fill="#555"/></svg>Work order</div>
<div class="abs nav" style="left:807px"><svg viewBox="0 0 10 10"><circle cx="5" cy="3" r="2.5" fill="#555"/><rect x="1" y="6" width="8" height="4" fill="#555"/></svg>Custom</div>
<div class="abs nav" style="left:884px"><svg viewBox="0 0 10 10"><circle cx="4" cy="4" r="3" fill="none" stroke="#555" stroke-width="1.5"/><line x1="6" y1="6" x2="9.5" y2="9.5" stroke="#555" stroke-width="1.8"/></svg>My View</div>
<div class="abs nav" style="left:957px"><svg viewBox="0 0 10 10"><line x1="1" y1="9" x2="8" y2="2" stroke="#555" stroke-width="2"/></svg>Help</div>
<div class="abs nav logoff" style="left:1039px;top:18px"><svg viewBox="0 0 10 10"><path d="M3 2.5A4 4 0 1 0 7 2.5" fill="none" stroke="#1a3f9c" stroke-width="1.4"/><line x1="5" y1="0" x2="5" y2="5" stroke="#1a3f9c" stroke-width="1.4"/></svg>LOG OFF</div>

<div class="abs sidebar"></div>
<div class="abs vtab" style="top:74px;height:67px;background:var(--orange)">TREEVIEW</div>
<div class="abs vtab" style="top:152px;height:78px;background:var(--side-tab)">WORKSPACE</div>
<div class="abs vtab" style="top:242px;height:78px;background:var(--side-tab)">ZONVIA</div>

<div class="abs tree"></div>
<div class="abs treemode">Tree Mode: <b>Today</b></div>
<div class="abs brand">Kelvox</div>

<div class="abs node big" style="left:58px;top:155px"><span class="pm">−</span><span class="folder"></span> Real Network</div>
<div class="abs node" style="left:73px;top:175px"><span class="pm">−</span>~ NORVIK</div>
<div class="abs node" style="left:88px;top:190px"><span class="pm">+</span>~ 2G</div>
<div class="abs node" style="left:88px;top:205px"><span class="pm">+</span>~ 3G</div>
<div class="abs node" style="left:88px;top:220px"><span class="pm">+</span>~ <span class="hl">LTE</span></div>
<div class="abs node" style="left:88px;top:236px"><span class="pm">+</span>~ CORE PS</div>
<div class="abs node" style="left:88px;top:251px"><span class="pm">+</span>~ SAE-GW</div>
<div class="abs node" style="left:88px;top:266px"><span class="pm">+</span>~ MME</div>
<div class="abs node" style="left:73px;top:280px"><span class="pm">+</span><span class="ico"></span> HALWEN</div>
<div class="abs node" style="left:73px;top:294px"><span class="pm">+</span><span class="ico"></span> ERIKSUND</div>
<div class="abs node" style="left:73px;top:307px"><span class="pm">+</span><span class="ico"></span> ZQN</div>
<div class="abs node" style="left:73px;top:321px"><span class="pm">+</span><span class="ico"></span> SELMAR</div>
<div class="abs node" style="left:73px;top:334px"><span class="pm">+</span><span class="ico"></span> MULTIVENDOR</div>
<div class="abs node" style="left:73px;top:348px"><span class="pm">+</span><span class="ico"></span> ALTREX</div>
<div class="abs node big" style="left:58px;top:368px"><span class="pm">−</span><span class="folder"></span> Planned Network</div>
<div class="abs node" style="left:74px;top:388px"><span class="pm">+</span><span class="folder"></span> Public Network</div>
<div class="abs node" style="left:74px;top:404px"><span class="pm">+</span><span class="folder"></span> Private Network</div>

<div class="abs tabstrip" style="left:252px;width:176px;background:#f4f4f4;justify-content:space-between;padding:0 10px;color:var(--link);font-size:8.5px"><span>( New Tab )</span><span style="color:#999">+ ×</span></div>
<div class="abs tabstrip" style="left:435px;width:64px;background:#e6e6e6;color:#444">+ Tab</div>
<div class="abs tabstrip" style="left:498px;width:14px"><svg width="11" height="13" viewBox="0 0 11 13"><path d="M1 1h6l3 3v8H1z" fill="none" stroke="#d33" stroke-width="1.2"/></svg></div>
<div class="abs tabstrip" style="left:521px;width:54px;background:#e1e1e1;color:#555">Go All</div>

<div class="abs prefs-outer"></div>
<div class="abs prefs-teal"></div>
<div class="abs prefs-white"></div>
<div class="abs ptitle">+ &nbsp;× &nbsp; Account Preferences</div>
<div class="abs save">SAVE</div>
<div class="abs itab on" style="left:264px;width:114px">User preferences</div>
<div class="abs itab" style="left:386px;width:114px">Chat preferences</div>
<div class="abs itab" style="left:509px;width:113px">Infer preferences</div>
<div class="abs tabline"></div>

<div class="abs lbl" style="left:274px;top:205px">User Name:</div>
<div class="abs inp" style="left:354px;top:199px"></div>
<div class="abs lbl" style="left:547px;top:205px">Full Name :</div>
<div class="abs inp" style="left:614px;top:199px"></div>
<div class="abs lbl" style="left:815px;top:205px">Phone No.</div>
<div class="abs inp" style="left:877px;top:199px"></div>

<div class="abs lbl" style="left:274px;top:247px">E-mail :</div>
<div class="abs inp" style="left:354px;top:241px"></div>
<div class="abs lbl" style="left:546px;top:247px">Old :<br>Password:</div>
<div class="abs inp" style="left:614px;top:241px"></div>
<div class="abs lbl" style="left:809px;top:247px">New<br>Password:</div>
<div class="abs inp" style="left:877px;top:241px"></div>

<div class="abs lbl" style="left:276px;top:286px">Repeate<br>Password :</div>
<div class="abs inp" style="left:354px;top:285px"></div>
<div class="abs lbl" style="left:546px;top:293px">Receive &nbsp;update emails :</div>
<div class="abs radio" style="left:670px;top:296px"><i class="on"></i><b style="font-weight:600">Yes</b></div>
<div class="abs radio" style="left:720px;top:296px"><i></i><b style="font-weight:600">No</b></div>
<div class="abs submit">SUBMIT</div>

<div class="abs tt-head">+ &nbsp;× &nbsp; TROUBLE TICKETS (TT)</div>
<div class="abs btn" style="left:247px;width:30px">NEW</div>
<div class="abs btn" style="left:284px;width:93px">SHOW MONITORED</div>
<div class="abs" style="left:461px;top:462px;font-size:8.5px;color:var(--link)">⊞ Text or ID:</div>
<div class="abs field"></div>
<div class="abs btn" style="left:628px;width:52px">SHOW TT</div>

<div class="abs bar" style="top:491px"><svg width="6" height="8" viewBox="0 0 6 8"><path d="M1 0l4 4-4 4z" fill="#555"/></svg>Selected TT</div>
<div class="abs bar" style="top:538px"><svg width="8" height="6" viewBox="0 0 8 6"><path d="M0 1h8L4 5z" fill="#555"/></svg>Search Results</div>
<div class="abs filter">FILTER RESULTS</div>

<table>
  <colgroup><col style="width:21px"><col style="width:45px"><col style="width:32px"><col style="width:69px"><col style="width:53px"><col style="width:131px"><col style="width:132px"><col style="width:186px"><col style="width:124px"><col style="width:144px"></colgroup>
  <thead><tr><th></th><th>ID</th><th>N</th><th>Priority</th><th>Days</th><th>Status</th><th>Problem ID</th><th>Description</th><th>Updated</th><th>Opened By</th></tr></thead>
  <tbody>
    <tr class="red"><td><span class="chk"></span></td><td>1582</td><td>2</td><td>None</td><td>7</td><td>Feedback<br>[Kelvox] support team</td><td>New Feature Request</td><td>Duis aute irure dolor in repre</td><td>25-01-2014</td><td>[Kelvox] support<br>_team</td></tr>
    <tr><td><span class="chk"></span></td><td>1582</td><td>2</td><td>None</td><td>7</td><td>Feedback<br>[Kelvox] support team</td><td>New Feature Request</td><td>Duis aute irure dolor in repre</td><td>25-01-2014</td><td>[Kelvox] support<br>_team</td></tr>
    <tr class="lav"><td><span class="chk" style="background:#aaa"></span></td><td>1582</td><td>2</td><td>None</td><td>7</td><td>Feedback<br>[Kelvox] support team</td><td>New Feature Request</td><td>Duis aute irure dolor in repre</td><td>25-01-2014</td><td>[Kelvox] support<br>_team</td></tr>
    <tr class="red"><td><span class="chk"></span></td><td>1582</td><td>2</td><td>None</td><td>7</td><td>Feedback<br>[Kelvox] support team</td><td>New Feature Request</td><td>Duis aute irure dolor in repre</td><td>25-01-2014</td><td>[Kelvox] support<br>_team</td></tr>
    <tr><td><span class="chk"></span></td><td>1582</td><td>2</td><td>None</td><td>7</td><td>Feedback<br>[Kelvox] support team</td><td>New Feature Request</td><td>Duis aute irure dolor in repre</td><td>25-01-2014</td><td>[Kelvox] support<br>_team</td></tr>
    <tr class="lav"><td><span class="chk" style="background:#aaa"></span></td><td>1582</td><td>2</td><td>None</td><td>7</td><td>Feedback<br>[Kelvox] support team</td><td>New Feature Request</td><td>Duis aute irure dolor in repre</td><td>25-01-2014</td><td>[Kelvox] support<br>_team</td></tr>
    <tr class="red"><td><span class="chk"></span></td><td>1582</td><td>2</td><td>None</td><td>7</td><td>Feedback<br>[Kelvox] support team</td><td>New Feature Request</td><td>Duis aute irure dolor in repre</td><td>25-01-2014</td><td>[Kelvox] support<br>_team</td></tr>
  </tbody>
</table>

<div class="abs footer"></div>
<div class="abs" style="left:479px;top:1052px;color:#fff;font-size:10.5px">Copyright © 2014 Yoursite. All rights reserved.</div>
<div class="abs" style="left:1135px;top:1052px;color:#fff;font-size:10.5px">x 6</div>

</body>
</html>
```